Business card design needed with logo

My business is called KVM Solutions & it is targeted towards mobile equipment maintenance in the Mining and civil industry. My work involves maintenance planning and maintenance management plus also supply tradespeople on a labour hire basis. We can provide from basic shut-down machine rebuild plans to complete rebuild services supply plans and labour to anywhere in Australia. I would like to use the colours Black, Red and Grey, I had done a desgin as attached but doesn't really explain what we do and gears don't embroider well onto shirts.
Updates

I also wanted to see the something replace the gears maybe just making the KVM lettering look a bit different or put together differently 

Hello I have extended the deadline by a few extra days as I would like to update details on the front of card, details below & can be put which ever way looks good;

Liam Fenwick
Director
0417263958
KVM@mailnest.com.au
www.kvmsolutions-demo.com.au

On the back of the card I would like to have the below printed;

Capable of providing, but not limited to, across Australia:
- Contract Maintenance Planning.
- Skilled Mobile Maintenance labour hire.
- New machine build specifications. 
- Plant risk assessments and inspections.
- Shut down and rebuild program planning.
- Preventative maintenance tasks, including build of materials lists, creation and review.

Target Market(s)

Contractors and companies that use small and large earthmoving and mining machines

Industry/Entity Type

Business

Contact Information for Business Card

Trading name is KVM Solutions
My name and title is
Liam Fenwick Director
0417 263 958
KVM@mailnest.com.au

Logo Text

KVM

```html
<!DOCTYPE html>
<html lang="en">
<head>
<meta charset="utf-8">
<title>KVM Solutions – Business Card</title>
<link href="https://fonts.googleapis.com/css2?family=Nunito:wght@400;600;800&display=swap" rel="stylesheet">
<style>
  :root {
    --page-bg: #ececec;
    --card-black: #070909;
    --metal-dark: #2a2b2c;
    --metal-mid: #4a4b4d;
    --brand-red: #de1f26;
    --brand-grey: #c9c9c9;
    --text-white: #ffffff;
    --text-dark: #1c1c1c;
  }
  html, body {
    margin: 0;
    padding: 0;
    width: 1200px;
    height: 1000px;
    overflow: hidden;
    background: var(--page-bg);
    font-family: "Nunito", sans-serif;
  }
  .canvas {
    position: relative;
    width: 1200px;
    height: 1000px;
  }
  .business-card {
    position: absolute;
    left: 89px;
    top: 213px;
    width: 1022px;
    height: 574px;
    background: var(--card-black);
    overflow: hidden;
  }
  .metal-panel {
    position: absolute;
    left: 0;
    width: 100%;
  }
  .metal-panel--top {
    top: 0;
    height: 137px;
    background: linear-gradient(180deg, var(--metal-dark), #1a1b1c);
  }
  .metal-panel--bottom {
    bottom: 0;
    height: 142px;
    background: linear-gradient(180deg, var(--metal-mid), #2f3031);
  }
  .brand-name {
    position: absolute;
    left: 96px;
    top: 248px;
    display: flex;
    align-items: center;
    gap: 16px;
    margin: 0;
    color: var(--brand-red);
    font-weight: 800;
    font-size: 58px;
    line-height: 1;
    letter-spacing: -0.5px;
  }
  .brand-name__mark {
    width: 26px;
    height: 26px;
    background: var(--brand-grey);
    flex: none;
  }
  .name-tab {
    position: absolute;
    left: 628px;
    top: 191px;
    width: 394px;
    height: 106px;
  }
  .contact-name {
    position: absolute;
    right: 66px;
    top: 206px;
    margin: 0;
    color: var(--text-white);
    font-weight: 800;
    font-size: 34px;
    line-height: 1;
  }
  .contact-title {
    position: absolute;
    right: 66px;
    top: 252px;
    margin: 0;
    color: var(--text-dark);
    font-weight: 800;
    font-size: 27px;
    line-height: 1;
  }
  .contact-details {
    position: absolute;
    right: 66px;
    top: 316px;
    margin: 0;
    text-align: right;
    color: var(--text-white);
    font-weight: 400;
    font-size: 31px;
    line-height: 42px;
  }
</style>
</head>
<body>
<main class="canvas">
  <section class="business-card">
    <div class="metal-panel metal-panel--top" role="img" aria-label="Perforated brushed metal texture"></div>
    <div class="metal-panel metal-panel--bottom" role="img" aria-label="Perforated brushed metal texture"></div>

    <h1 class="brand-name"><span class="brand-name__mark"></span>KVM Solutions</h1>

    <svg class="name-tab" viewBox="0 0 394 106" aria-hidden="true">
      <polygon points="72,0 394,0 394,106 0,106" fill="var(--brand-red)"/>
    </svg>
    <p class="contact-name">Liam Fenwick</p>
    <p class="contact-title">Director</p>

    <p class="contact-details">
      0417 263 958<br>
      KVM@mailnest.com.au
    </p>
  </section>
</main>
</body>
</html>
```